Business Card Design for Cybersecurity Company - Quorvent Systems

We need a business card design for our new cybersecurity company, Quorvent. We’re going for a clean, hi tech look that feels modern, premium, and trustworthy. We want a design that really stands out and makes people say WOW when we hand it over!

Quorvent delivers reliable IT support and managed services for small and mid sized businesses. We help companies stay secure, efficient, and connected through proactive monitoring, cybersecurity services, cloud management, and remote support.

Target Market(s)

Designers should target small and mid sized businesses that need dependable cybersecurity and IT support.

Industry/Entity Type

Cybersecurity, Managed Service Provider, IT services

Contact Information for Business Card

Contact information

Requirements
Must have
• The card should look clean, modern, and tech focused, with the Quorvent logo, clear contact info, and strong readability. It needs to feel premium and professional while still keeping a simple layout that fits a cybersecurity and IT brand.
Nice to have
• Nice to have elements include subtle touches that give the card a modern, tech feel, along with a layout that works well in different background styles.
Should not have
• The card should avoid clutter, loud graphics, or anything that takes attention away from the logo and contact details.

```html
<!DOCTYPE html>
<html lang="en">
<head>
<meta charset="utf-8">
<title>Quorvent Systems — Business Card</title>
<link rel="stylesheet" href="https://fonts.googleapis.com/css2?family=Arimo:wght@400;700&family=Montserrat:wght@600&display=swap">
<style>
  :root {
    --page-bg: #e4e4e6;
    --card-white: #ffffff;
    --brand-blue: #3d5ef0;
    --brand-indigo: #5146e6;
    --brand-purple: #7420d6;
    --text-grey: #4a4a4f;
    --divider-grey: #5a5a60;
    --back-edge: #3168f7;
    --back-center: #7424d8;
  }
  * { margin: 0; padding: 0; box-sizing: border-box; }
  html, body {
    width: 1200px; height: 1200px; overflow: hidden;
    background: var(--page-bg);
    font-family: "Arimo", Arial, sans-serif;
  }
  .card {
    position: absolute; left: 255px;
    width: 690px; height: 394px;
    overflow: hidden;
  }
  .card-front { top: 158px; background: var(--card-white); }
  .card-back {
    top: 653px;
    background: radial-gradient(ellipse 55% 90% at 50% 45%, var(--back-center) 0%, #5a3be6 45%, var(--back-edge) 100%);
  }

  .brand {
    position: absolute; left: 104px; top: 176px;
    display: flex; align-items: center; gap: 12px;
  }
  .brand-dot {
    width: 14px; height: 14px; border-radius: 50%;
    background: var(--brand-indigo);
  }
  .brand-name {
    font-family: "Montserrat", Arial, sans-serif;
    font-weight: 600; font-size: 36px; color: var(--brand-indigo);
    letter-spacing: 0.5px;
  }

  .divider {
    position: absolute; left: 376px; top: 124px;
    width: 1.6px; height: 154px;
    background: var(--divider-grey);
  }

  .contact-block { position: absolute; left: 405px; top: 118px; }
  .person-name {
    font-weight: 700; font-size: 27px; color: var(--brand-blue);
    line-height: 1;
  }
  .person-role {
    margin-top: 8px; font-size: 15.5px; color: var(--brand-purple);
  }
  .contact-list { list-style: none; margin-top: 22px; }
  .contact-item {
    display: flex; align-items: center; height: 20.5px;
    font-size: 16.5px; color: var(--text-grey);
  }
  .contact-icon { width: 14px; height: 14px; margin-right: 12px; flex: none; }

  .back-brand {
    position: absolute; left: 0; right: 0; top: 150px;
    text-align: center;
    font-family: "Montserrat", Arial, sans-serif;
    font-weight: 600; font-size: 40px; color: rgba(255,255,255,0.22);
  }
  .back-url {
    position: absolute; left: 0; right: 0; top: 330px;
    text-align: center; font-size: 16px; color: #ffffff;
  }
</style>
</head>
<body>

<section class="card card-front" aria-label="Card front">
  <div class="brand">
    <span class="brand-dot"></span>
    <span class="brand-name">Quorvent</span>
  </div>

  <div class="divider" aria-hidden="true"></div>

  <div class="contact-block">
    <h1 class="person-name">Dana Whitlock</h1>
    <p class="person-role">Owner | CEO</p>
    <ul class="contact-list">
      <li class="contact-item">
        <svg class="contact-icon" viewBox="0 0 24 24" aria-hidden="true"><path fill="#3d5ef0" d="M6.6 10.8a15.1 15.1 0 0 0 6.6 6.6l2.2-2.2a1 1 0 0 1 1-.25 11.4 11.4 0 0 0 3.6.57 1 1 0 0 1 1 1V20a1 1 0 0 1-1 1A17 17 0 0 1 3 4a1 1 0 0 1 1-1h3.5a1 1 0 0 1 1 1c0 1.25.2 2.45.57 3.57a1 1 0 0 1-.25 1z"/></svg>
        (855) 555-0142
      </li>
      <li class="contact-item">
        <svg class="contact-icon" viewBox="0 0 24 24" aria-hidden="true"><rect x="6" y="2" width="12" height="20" rx="2" fill="none" stroke="#3d5ef0" stroke-width="2.4"/><line x1="10" y1="18" x2="14" y2="18" stroke="#3d5ef0" stroke-width="2"/></svg>
        (813) 555-0187
      </li>
      <li class="contact-item">
        <svg class="contact-icon" viewBox="0 0 24 24" aria-hidden="true"><rect x="2" y="5" width="20" height="14" fill="#3d5ef0"/><path d="M2 5l10 8 10-8" fill="none" stroke="#fff" stroke-width="1.8"/></svg>
        dana@quorvent.com
      </li>
      <li class="contact-item">
        <svg class="contact-icon" viewBox="0 0 24 24" aria-hidden="true"><circle cx="12" cy="12" r="10" fill="#3d5ef0"/><path d="M7 6c2 1 3 3 2 5s-3 2-3 4M15 4c-1 2 0 3 2 4s2 3 1 5M13 20c0-2 1-3 3-3" fill="none" stroke="#fff" stroke-width="1.5"/></svg>
        www.quorvent.com
      </li>
    </ul>
  </div>
</section>

<section class="card card-back" aria-label="Card back">
  <div class="back-brand">Quorvent</div>
  <p class="back-url">www.quorvent.com</p>
</section>

</body>
</html>
```